Business Card Design for Clinical Therapist

I will operate in 3 product areas as follows...
I will operate as Psychotherapist providing an opportunity for individuals to stop, reflect, heal, and gain hope in a safe and professional atmosphere. My task as a Licensed Mental Health Social Worker is to work “along-side” the client to help guide them toward answers they may seek. I believe that all difficulties contain a small seed of opportunity within them and I can support the individual in clarifying issues while resolving obstacles that may get in the way.
1-Therapy
Treatment Issues may include:
• Addiction
• Bipolar Disorder
• Adolescent or Adult
• Coping Skills
• Dual Diagnosis
• Family Conflict
• Sleep or Insomnia
• Substance Abuse
• Anger Management
• Career Counseling
• Drug Abuse
• Emotional Disturbance
• Grief
• Self Esteem
• Trauma and PTSD
Treatment Orientation may include but not be limited to:
• CBT
• EMDR
• Person-Centered
• Mindfulness based (MBCT)
• Motivational Interviewing

2-Other Substance Abuse Services
SAP Assessments
Employees performing safety-sensitive duties under US Bureau of Roadway Affairs rules must have an evaluation by a qualified Substance Abuse Professional when they are in violation of BRA rules (for a positive test or a refusal to test). I am a BRA qualified SAP and can perform these evaluations, which involve specialized assessment and compliance reports, as well as a return to work assessment.

3-DUI/OVUII Assessments
Substance abuse assessment reports-State level assessments targeted for the court system.

Somehow I would like the final design to acknowledge the three areas of services, or two being therapy for mental health services and combining SAP/OVUII assessment reporting for Substance abuse)

Industry/Entity Type

Mental Health

Contact Information for Business Card

Brightwell Harbor LLC,
Desmond Farrowby LCSW
Clinical Therapist
2087 West Palmer Avenue, STE 412
Honolulu, HI 96720
808.555.0193
brightwellharborllc.example

Colors

Designer to choose colors to be used in the design.

```html
<!DOCTYPE html>
<html lang="en">
<head>
<meta charset="utf-8">
<title>Brightwell Harbor LLC — Business Card</title>
<link rel="stylesheet" href="https://fonts.googleapis.com/css2?family=Oswald:wght@700&family=Arimo:ital,wght@0,400;0,700;1,400&display=swap">
<style>
  :root {
    --page-bg: #ffffff;
    --label-grey: #6d6d6d;
    --ink: #1a1a1a;
    --ink-soft: #2b2b2b;
    --white: #ffffff;
    --night: #000000;
    --deep-blue: #0a2a8c;
    --bright-blue: #2f6bff;
    --glow-blue: #7fb0ff;
    --frame-blue: #5d86c9;
  }
  * { box-sizing: border-box; margin: 0; padding: 0; }
  html, body {
    width: 1200px; height: 1200px; overflow: hidden;
    background: var(--page-bg);
    font-family: "Arimo", Arial, sans-serif;
  }
  .sheet { position: relative; width: 1200px; height: 1200px; }

  .side-label {
    position: absolute;
    font-size: 26px; color: var(--label-grey);
  }
  .side-label--front { left: 184px; top: 96px; }
  .side-label--back { left: 236px; top: 566px; }

  /* Front */
  .card-front {
    position: absolute; left: 180px; top: 136px;
    width: 704px; height: 404px; overflow: hidden;
    background: var(--night);
  }
  .card-front__waves {
    position: absolute; inset: 0;
    background:
      radial-gradient(ellipse 70% 22% at 30% 62%, rgba(127,176,255,0.55) 0%, rgba(47,107,255,0.25) 45%, transparent 75%),
      radial-gradient(ellipse 60% 30% at 20% 85%, rgba(47,107,255,0.9) 0%, rgba(10,42,140,0.6) 50%, transparent 80%),
      radial-gradient(ellipse 80% 25% at 75% 95%, rgba(47,107,255,0.7) 0%, transparent 70%),
      linear-gradient(180deg, var(--night) 0%, #02061a 35%, var(--deep-blue) 75%, #0c3bb8 100%);
  }
  .service-list {
    position: absolute; right: 46px; top: 44px;
    text-align: right; list-style: none;
    font-family: "Oswald", "Arial Narrow", sans-serif; font-weight: 700;
    font-size: 38px; line-height: 60px; color: var(--white);
  }
  .contact {
    position: absolute; left: 20px; top: 274px;
    color: var(--white); font-weight: 700;
    font-variant: small-caps; font-size: 17px; line-height: 23px;
    font-style: normal;
  }
  .contact__web { font-size: 13px; letter-spacing: 0.5px; margin-top: 2px; }

  /* Back */
  .card-back {
    position: absolute; left: 314px; top: 566px;
    width: 702px; height: 400px; overflow: hidden;
    background: var(--white);
    box-shadow: inset 0 0 40px 18px var(--frame-blue), inset 0 0 0 3px #1d3f7a;
    color: var(--ink);
  }
  .about {
    position: absolute; left: 32px; top: 22px; width: 620px;
    font-style: italic; font-size: 17px; line-height: 22px; color: var(--ink-soft);
  }
  .about p + p { margin-top: 12px; }
  .treatments-title {
    position: absolute; left: 0; width: 702px; top: 208px;
    text-align: center; font-weight: 700; font-variant: small-caps;
    font-size: 18px; line-height: 22px; color: var(--ink);
  }
  .treatments-title span { border-bottom: 2px solid var(--ink); }
  .issue-list {
    position: absolute; list-style: none;
    font-size: 15px; line-height: 18.5px; color: var(--ink);
  }
  .issue-list li::before { content: "• "; }
  .issue-list--a { left: 22px; top: 234px; }
  .issue-list--b { left: 244px; top: 234px; }
  .orientation {
    position: absolute; left: 478px; top: 234px;
    font-size: 13px; line-height: 16px; color: var(--ink);
  }
  .orientation .issue-list { position: static; margin-top: 2px; }
</style>
</head>
<body>
<main class="sheet">
  <div class="side-label side-label--front">Front</div>
  <section class="card-front">
    <div class="card-front__waves" role="img" aria-label="Flowing blue light waves across a black background"></div>
    <ul class="service-list">
      <li>THERAPY</li>
      <li>SUBSTANCE ABUSE SERVICES</li>
      <li>DUI/OVUII ASSESSMENTS</li>
    </ul>
    <address class="contact">
      <div>Brightwell Harbor LLC,</div>
      <div>Desmond Farrowby LCSW Clinical Therapist</div>
      <div>2087 West Palmer Avenue, STE 412 Honolulu, HI 96720</div>
      <div>808.555.0193</div>
      <div class="contact__web">BRIGHTWELLHARBORLLC.EXAMPLE</div>
    </address>
  </section>

  <div class="side-label side-label--back">Back</div>
  <section class="card-back">
    <div class="about">
      <p>I am a Psychotherapist providing an opportunity for individuals to stop, reflect, heal, and gain hope in a safe and professional atmosphere.</p>
      <p>My task as a Licensed Mental Health Social Worker is to work “along-side” you, the client to help guide you toward answers you may seek.</p>
      <p>I believe that all difficulties contain a small seed of opportunity within them and I can support the individual in clarifying issues while resolving obstacles that may get in the way.</p>
    </div>
    <h2 class="treatments-title"><span>Therapy Treatments Offered:</span></h2>
    <ul class="issue-list issue-list--a">
      <li>Addiction</li>
      <li>Bipolar Disorder</li>
      <li>Adolescent or Adult</li>
      <li>Coping Skills</li>
      <li>Dual Diagnosis</li>
      <li>Family Conflict</li>
      <li>Sleep or Insomnia</li>
      <li>Substance Abuse</li>
    </ul>
    <ul class="issue-list issue-list--b">
      <li>Anger Management</li>
      <li>Career Counseling</li>
      <li>Drug Abuse</li>
      <li>Emotional Disturbance</li>
      <li>Grief</li>
      <li>Self Esteem</li>
      <li>Trauma and PTSD</li>
    </ul>
    <div class="orientation">
      <div>Treatment Orientation may<br>include but not be limited to:</div>
      <ul class="issue-list">
        <li>CBT</li>
        <li>EMDR</li>
        <li>Person-Centered</li>
        <li>Mindfulness based</li>
        <li>Motivational Interviewing</li>
      </ul>
    </div>
  </section>
</main>
</body>
</html>
```